Website for company called VELQUOgen

We need a website for our new company called VELQUOgen which developed a platform/technology to identify antigen-specific T cells (immune cells) which can be used for cancer therapy, autoimmunity, etc.

The platform is called VELQUO and is rapid, versatile, unbiased, and inexpensive.

We have a semi-final logo although we are not completely set on color and font of text (attached).

Target Market(s)

Our target audience at the moment would be potential investors and VCs. We eventually are interested in getting attention from scientists and cell/immunotherapy companies.

Industry/Entity Type

Healthcare/Technology

Coding

Coded - Design and coding required

Number of Pages Required

1 page

Colors
0094D4
00A9DD
6FCCEA
C7EBF8
E9F6FB
00AB8E
00BBA5
67D7C9
C6EFE9
E9F9F6
E54698
E96AAD
F1A4CE
F9D9EA
FCEFF6
A7469A
B969AE
D3A5CF
EDDBEB
F8F0F9
6B429C
8869AF
B7A5CE
E3DAEB
F3F0F8

Requirements
Must have
• Landing page about the company, About us page, Technology page (could be merged with company landing page), Contact us page

```html
<!DOCTYPE html>
<html lang="en">
<head>
<meta charset="utf-8">
<title>VELQUOgen — T Cell Discovery</title>
<link href="https://fonts.googleapis.com/css2?family=Poppins:wght@300;400;500;600&display=swap" rel="stylesheet">
<style>
:root{
  --blue:#0094D4;
  --blue-2:#00A9DD;
  --teal:#00AB8E;
  --teal-2:#00BBA5;
  --teal-soft:#C6EFE9;
  --ink:#1c1f2a;
  --text:#555a66;
  --tint:#eef3fb;
  --card-tint:#f0f4fb;
  --footer:#1b1e2b;
  --star:#00BBA5;
}
*{box-sizing:border-box;margin:0;padding:0}
html,body{width:1200px;height:3629px;overflow:hidden}
body{font-family:'Poppins',sans-serif;color:var(--ink);background:#fff;position:relative}
.abs{position:absolute}
.btn{position:absolute;background:var(--blue);color:#fff;font-size:13px;font-weight:500;display:flex;align-items:center;justify-content:center;border-radius:3px;width:161px;height:41px}
.label{position:absolute;left:0;width:1200px;text-align:center;color:var(--teal);font-size:13px}
.heading{position:absolute;left:0;width:1200px;text-align:center;font-size:31px;font-weight:500}
.sub{position:absolute;left:0;width:1200px;text-align:center;font-size:13.5px;color:var(--text);line-height:20px}

/* header & hero */
.hero{position:absolute;left:0;top:0;width:1200px;height:648px;overflow:hidden;
  background:linear-gradient(90deg,#f4f6f9 0%,#eceff4 38%,#c9d6e6 62%,#8fa8c8 85%,#6f8fb8 100%)}
.hero-photo{position:absolute;left:0;top:0;width:1200px;height:648px;
  background:radial-gradient(ellipse 420px 360px at 900px 260px,rgba(180,200,225,.7),transparent 70%),
  radial-gradient(ellipse 300px 200px at 1000px 560px,rgba(40,110,200,.55),transparent 70%)}
.topbar{position:absolute;left:0;top:0;width:1200px;height:70px;background:rgba(255,255,255,.55)}
.brand{position:absolute;left:162px;top:24px;display:flex;align-items:center;gap:8px;font-size:26px;font-weight:500;color:var(--ink)}
.brand .dot{width:14px;height:14px;border-radius:50%;background:var(--blue)}
.nav{position:absolute;top:35px;font-size:12.5px;color:#333}
.nav.active{color:var(--blue)}
.hero h1{position:absolute;left:158px;top:206px;font-size:44px;font-weight:500;line-height:51px;width:520px}
.hero h1 em{font-style:normal;color:var(--teal);font-weight:600}
.hero p{position:absolute;left:160px;top:376px;width:500px;font-size:13.5px;line-height:18px;color:#333}
.pill{position:absolute;left:888px;top:438px;width:180px;height:34px;border-radius:17px;background:#fff;display:flex;align-items:center;gap:10px;padding-left:10px;font-size:13px;box-shadow:0 2px 6px rgba(0,0,0,.1)}
.pill .avatar{width:22px;height:22px;border-radius:50%;background:#c7d2de}
.quote-card{position:absolute;left:690px;top:490px;width:375px;height:100px;background:var(--blue);border-radius:14px;transform:skewX(-4deg);box-shadow:-8px 8px 0 #fff}
.quote-card p{position:absolute;left:34px;top:26px;width:320px;font-size:13px;line-height:16px;color:#fff;transform:skewX(4deg)}
.quote-mark{position:absolute;left:1000px;top:478px;font-size:40px;font-weight:600;color:var(--teal-2);line-height:40px}
.hero-dash{position:absolute;top:616px;height:2px;width:14px;background:#fff}

/* tech */
.tech{position:absolute;left:0;top:1006px;width:1200px;height:651px;background:var(--tint)}
.tcard{position:absolute;top:227px;width:261px;height:260px;background:#fff;border:1px solid #dde3ee;border-radius:4px;overflow:hidden}
.tcard h3{position:absolute;left:25px;top:36px;font-size:16.5px;font-weight:500}
.tcard p{position:absolute;left:25px;top:68px;width:200px;font-size:10.5px;line-height:16px;color:var(--text)}
.tcard .more{position:absolute;left:25px;top:129px;font-size:10.5px;color:var(--teal)}
.tcard .ring{position:absolute;left:135px;top:130px;width:150px;height:150px;border-radius:50%;background:var(--teal-soft)}
.tcard .thumb{position:absolute;left:145px;top:140px;width:140px;height:140px;border-radius:50%}
.dots{position:absolute;top:1530px;left:583px;display:flex;gap:6px;align-items:center}
.dots i{display:block;width:6px;height:6px;border-radius:50%;background:var(--teal)}
.dots i.on{width:14px;height:14px;border:2px solid var(--teal);background:#fff;box-shadow:inset 0 0 0 3px #fff,inset 0 0 0 8px var(--teal)}

/* banner */
.banner{position:absolute;left:0;top:1657px;width:1200px;height:416px;
  background:radial-gradient(ellipse 200px 160px at 870px 320px,#d9503f 0%,rgba(30,90,200,.6) 60%,transparent 100%),
  linear-gradient(135deg,#0b3f9a,#1f6fd6 45%,#0a3a8e)}
.banner-card{position:absolute;left:162px;top:79px;width:438px;height:259px;background:#fff;border-radius:10px}
.banner-card h2{position:absolute;left:34px;top:38px;font-size:31px;font-weight:500;line-height:31px}
.banner-card h2 span{font-size:23px}
.banner-card p{position:absolute;left:36px;top:114px;width:370px;font-size:11px;line-height:14px;color:#333}

/* testimonials */
.rcard{position:absolute;top:2288px;width:253px;height:253px;background:var(--card-tint)}
.rcard.faded{opacity:.45}
.stars{position:absolute;left:27px;top:30px;font-size:19px;letter-spacing:1px;color:var(--star)}
.rcard h4{position:absolute;left:27px;top:78px;font-size:15px;font-weight:500;line-height:18px;width:200px}
.rcard p{position:absolute;left:27px;top:130px;width:215px;font-size:11.5px;line-height:18px;color:#444}
.rcard p b{font-weight:400;color:var(--teal);text-decoration:underline}
.rcard .who{position:absolute;left:27px;top:196px;font-size:14px}
.rcard .where{position:absolute;left:27px;top:217px;font-size:11.5px;color:var(--teal)}
.arrow{position:absolute;top:2588px;width:32px;height:32px;border:1px solid #333;border-radius:50%}
.track{position:absolute;left:397px;top:2601px;width:406px;height:7px;border-radius:4px;background:#dde6f0}
.track i{position:absolute;left:52px;top:0;width:130px;height:7px;border-radius:4px;background:var(--blue)}

/* news */
.ncard{position:absolute;top:2835px;width:395px;height:334px;background:var(--card-tint);border-radius:6px}
.ncard .img{position:absolute;left:12px;top:11px;width:371px;height:213px;border-radius:6px}
.ncard h4{position:absolute;left:33px;top:251px;font-size:17px;font-weight:400;line-height:21px;width:320px}
.ncard .meta{position:absolute;left:33px;top:303px;font-size:11px;color:#444;display:flex;gap:44px}
.ncard .meta b{font-weight:400;color:var(--teal)}

/* footer */
.footer{position:absolute;left:0;top:3317px;width:1200px;height:312px;background:var(--footer);color:#fff}
.footer h5{position:absolute;top:57px;font-size:16px;font-weight:500}
.flink{position:absolute;left:377px;font-size:12px}
.fcontact{position:absolute;left:541px;display:flex;align-items:center;gap:10px;font-size:12.5px}
.fcontact .ic{width:27px;height:27px;border-radius:50%;background:var(--teal-2);display:flex;align-items:center;justify-content:center}
.femail{position:absolute;left:790px;top:99px;width:248px;height:36px;background:#fff;color:#999;font-size:12.5px;padding:9px 14px}
.fsub{position:absolute;left:790px;top:148px;width:102px;height:34px;background:var(--blue);font-size:12.5px;font-weight:500;display:flex;align-items:center;justify-content:center}
.fbrand{position:absolute;left:190px;top:110px;display:flex;align-items:center;gap:8px;font-size:19px;font-weight:500}
.fbrand .dot{width:12px;height:12px;border-radius:50%;background:var(--blue-2)}
.social{position:absolute;top:208px;width:14px;height:14px;border-radius:50%;border:1.5px solid #fff}
.fline{position:absolute;left:162px;top:258px;width:876px;height:1px;background:#3a3e4e}
.copy{position:absolute;left:0;top:276px;width:1200px;text-align:center;font-size:13px}
</style>
</head>
<body>

<section class="hero">
  <div class="hero-photo" role="img" aria-label="Scientist in protective suit and mask working at a microscope in a laboratory"></div>
  <div class="topbar"></div>
  <div class="brand"><span class="dot"></span>VELQUOgen</div>
  <span class="nav active" style="left:419px">HOME</span>
  <span class="nav" style="left:505px">ABOUT</span>
  <span class="nav" style="left:598px">TECHNOLOGY</span>
  <span class="nav" style="left:732px">TESTIMONIALS</span>
  <span class="nav" style="left:874px">NEWS</span>
  <span class="nav" style="left:958px">CONTACT US</span>

  <h1>Revolutionizing <em>T Cell Discovery</em> for Precision Immunotherapy</h1>
  <p>VELQUOgen's proprietary VELQUO platform enables the rapid, unbiased identification of antigen-specific T cells.</p>
  <div class="btn" style="left:161px;top:429px">Learn More</div>

  <div class="pill"><span class="avatar"></span>Mara Ellison</div>
  <div class="quote-mark">”</div>
  <div class="quote-card"><p>"If you are in need of high-quality, professional and friendly dental care, look no further than our clinic."</p></div>
  <span class="hero-dash" style="left:870px"></span>
  <span class="hero-dash" style="left:888px"></span>
</section>

<section>
  <div class="label" style="top:705px">About Us</div>
  <div class="heading" style="top:730px">About Us</div>
  <p class="sub" style="top:783px;left:227px;width:746px">It is a long established fact that a reader will be distracted by the readable content of a page when looking at its layout. The point of using Lorem Ipsum is that it has a more-or-less normal distribution of letters, as opposed to using 'Content here, content here', making it look like readable English. Many desktop publishing packages and web page editors now use Lorem Ipsum as their default model text, and a search for 'lorem ipsum' will uncover many web sites still in their infancy.</p>
  <div class="btn" style="left:520px;top:905px">Learn More</div>
</section>

<section class="tech">
  <div class="label" style="top:73px">Technology</div>
  <div class="heading" style="top:97px">Our Technology</div>
  <p class="sub" style="top:146px">Welcome to our BrightpathChapters dedicated to empowering pet owners with<br>valuable knowledge and resources.</p>

  <div class="tcard" style="left:54px"><h3>Antigen-Agnostic</h3><p>It is a long established fact that a reader will be distracted by when looking at its layout..</p><span class="more">LEARN MORE</span><span class="ring"></span><span class="thumb" role="img" aria-label="Laboratory test tubes with blue and amber liquids" style="background:linear-gradient(135deg,#e8eef6,#2f6fc4 55%,#d58a2a)"></span></div>
  <div class="tcard" style="left:330px"><h3>High-Throughput</h3><p>It is a long established fact that a reader will be distracted by when looking at its layout..</p><span class="more">LEARN MORE</span><span class="ring"></span><span class="thumb" role="img" aria-label="Illustration of an immune cell" style="background:radial-gradient(circle at 55% 55%,#e0584a 0 12%,#2a7fd0 40%,#0d3c8a)"></span></div>
  <div class="tcard" style="left:607px"><h3>Low Sample Input</h3><p>It is a long established fact that a reader will be distracted by when looking at its layout..</p><span class="more">LEARN MORE</span><span class="ring"></span><span class="thumb" role="img" aria-label="Researcher looking into a microscope" style="background:linear-gradient(135deg,#dfe6ee,#8fa3b8 60%,#2b3440)"></span></div>
  <div class="tcard" style="left:884px"><h3>Scalable &amp; Affordable</h3><p>It is a long established fact that a reader will be distracted by when looking at its layout..</p><span class="more">LEARN MORE</span><span class="ring"></span><span class="thumb" role="img" aria-label="Gloved hand holding a sample tube" style="background:linear-gradient(135deg,#f1f4f8,#5b90d8 55%,#d9b23a)"></span></div>

  <div class="btn" style="left:520px;top:559px">View All Technology</div>
</section>
<div class="dots"><i></i><i class="on"></i><i></i></div>

<section class="banner" role="img" aria-label="Microscopic rendering of blue virus particles with a glowing red core">
  <div class="banner-card">
    <h2>Harnessing The Power<br><span>of The Immune System</span></h2>
    <p>You can be assured – we have a commitment to excellence when it comes to the level of care we provide to each and every patient.</p>
    <div class="btn" style="left:37px;top:178px">Learn More</div>
  </div>
</section>

<section>
  <div class="label" style="top:2130px">Our Testimonial</div>
  <div class="heading" style="top:2155px">Our Greatest Achievement</div>
  <p class="sub" style="top:2207px">Welcome to our BrightpathChapters dedicated to empowering pet owners with<br>valuable knowledge and resources.</p>

  <div class="rcard faded" style="left:-63px"><div class="stars">★★★★★</div><h4>"This Whole Practice Is Wonderful!!"</h4><p>It is a long established fact that a reader will be distracted by the of using Lorem Ipsum. <b>READ MORE</b></p><div class="who">Noreen T.</div><div class="where">Elm Harbor</div></div>
  <div class="rcard" style="left:205px"><div class="stars">★★★★★</div><h4>"This Whole Practice Is Wonderful!!"</h4><p>It is a long established fact that a reader will be distracted by the of using Lorem Ipsum. <b>READ MORE</b></p><div class="who">Noreen T.</div><div class="where">Elm Harbor</div></div>
  <div class="rcard" style="left:473px"><div class="stars">★★★★★</div><h4>"This Whole Practice Is Wonderful!!"</h4><p>It is a long established fact that a reader will be distracted by the of using Lorem Ipsum. <b>READ MORE</b></p><div class="who">Noreen T.</div><div class="where">Elm Harbor</div></div>
  <div class="rcard" style="left:741px"><div class="stars">★★★★★</div><h4>"This Whole Practice Is Wonderful!!"</h4><p>It is a long established fact that a reader will be distracted by the of using Lorem Ipsum. <b>READ MORE</b></p><div class="who">Noreen T.</div><div class="where">Elm Harbor</div></div>
  <div class="rcard faded" style="left:1011px"><div class="stars">★★★★★</div><h4>"This Whole Practice Is Wonderful!!"</h4><p>It is a long established fact that a reader will be distracted by the of using Lorem Ipsum. <b>READ MORE</b></p><div class="who">Noreen T.</div><div class="where">Elm Harbor</div></div>

  <div class="arrow" style="left:326px"><svg width="32" height="32" viewBox="0 0 32 32"><path d="M18 11l-5 5 5 5" fill="none" stroke="#222" stroke-width="1.6"/></svg></div>
  <div class="track"><i></i></div>
  <div class="arrow" style="left:841px"><svg width="32" height="32" viewBox="0 0 32 32"><path d="M14 11l5 5-5 5" fill="none" stroke="#222" stroke-width="1.6"/></svg></div>
</section>

<section>
  <div class="label" style="top:2688px">Latest News</div>
  <div class="heading" style="top:2712px">Latest News</div>
  <p class="sub" style="top:2764px">Welcome to our BrightpathChapters dedicated to empowering pet owners with<br>valuable knowledge and resources.</p>

  <div class="ncard" style="left:191px">
    <div class="img" role="img" aria-label="Blue virus particle beside a glowing DNA helix" style="background:radial-gradient(circle at 35% 50%,#8fd0ff,#1e6fd0 45%,#0a3a8a)"></div>
    <h4>PTSD: Causes, Symptoms, &amp; When to Seek Treatment</h4>
    <div class="meta"><span>▭ 01 Jan 2025</span><span>⚲ Posted By <b>Admin</b></span></div>
  </div>
  <div class="ncard" style="left:612px">
    <div class="img" role="img" aria-label="Scientist in safety goggles placing a drop into a test tube" style="background:linear-gradient(135deg,#1a7fb0,#3aa7c9 45%,#c9846a 70%,#1d6f9a)"></div>
    <h4>PTSD: Causes, Symptoms, &amp; When to Seek Treatment</h4>
    <div class="meta"><span>▭ 01 Jan 2025</span><span>⚲ Posted By <b>Admin</b></span></div>
  </div>

  <div class="btn" style="left:520px;top:3215px">View All News</div>
</section>

<footer class="footer">
  <div class="fbrand"><span class="dot"></span>VELQUOgen</div>
  <span class="social" style="left:195px"></span>
  <span class="social" style="left:239px"></span>
  <span class="social" style="left:281px"></span>

  <h5 style="left:377px">Quick Links</h5>
  <span class="flink" style="top:102px">Home</span>
  <span class="flink" style="top:129px">About Us</span>
  <span class="flink" style="top:156px">Technology</span>
  <span class="flink" style="top:183px">News</span>
  <span class="flink" style="top:210px">Contact Us</span>

  <h5 style="left:541px">Contact Us</h5>
  <div class="fcontact" style="top:97px"><span class="ic"><svg width="13" height="13" viewBox="0 0 24 24"><path d="M6.6 10.8a15 15 0 006.6 6.6l2.2-2.2c.3-.3.7-.4 1-.2 1.1.4 2.3.6 3.6.6.6 0 1 .4 1 1V20c0 .6-.4 1-1 1A17 17 0 013 4c0-.6.4-1 1-1h3.5c.6 0 1 .4 1 1 0 1.3.2 2.5.6 3.6.1.3 0 .7-.2 1z" fill="#fff"/></svg></span>+1 555 014 2290</div>
  <div class="fcontact" style="top:137px"><span class="ic"><svg width="13" height="13" viewBox="0 0 24 24"><rect x="3" y="6" width="18" height="12" rx="1" fill="none" stroke="#fff" stroke-width="2"/><path d="M3 7l9 6 9-6" fill="none" stroke="#fff" stroke-width="2"/></svg></span>hello@velquogen.example</div>
  <div class="fcontact" style="top:175px"><span class="ic"><svg width="13" height="13" viewBox="0 0 24 24"><path d="M12 2a7 7 0 00-7 7c0 5 7 13 7 13s7-8 7-13a7 7 0 00-7-7zm0 9.5A2.5 2.5 0 1112 6.5a2.5 2.5 0 010 5z" fill="#fff"/></svg></span>122, Lorem ipsum dolird</div>

  <h5 style="left:790px">Subscribe To Our Newsletter</h5>
  <div class="femail">E-mail</div>
  <div class="fsub">SUBSCRIBE</div>

  <div class="fline"></div>
  <div class="copy">Copyright © 2025velquogen. All rights reserved.</div>
</footer>

</body>
</html>
```